TIKLOOMTOT WEBSITE DESIGN

We need a website design based on the template- http://varolapixels.com/themes/quartzpage-bootstrap-wordpress-theme/. We purchased template and will build the website using wordpress. It is one page application. We wanted to list all content in one page and make it browser friendly (can be viewed in cell phone, pc, mac, ipad, etc).

The target audience is parents with babies/kids age from 0-5 year old. We wanted to sell the subscription based monthly boxes to the families. The box will include books, toys, crafts, kids consumer products and letter/note/card to the family from the experts. All boxes are customized based on children's age, gender and interests.

We wanted the site main color to be blue.

Please refer to these websites for ideas.
froxi.com
wwws.pebbleharbor.com
http://www.wigglyoats.com/

I've updated the project brief and make the project fund guaranteed. Thanks!

Target Market(s)

Parents with kids age from 0-5 years old. Mainly target to the China market.

Industry/Entity Type

Cell Phone

Colors
3277b5
85abd2
85cae6
33a6d7
0592cd
0355a3
ceddec
cee9f5

Requirements
Must have
• Must provide the design based on the template- http://varolapixels.com/themes/quartzpage-bootstrap-wordpress-theme/.
The site has to be Chinese character friendly since we are going to post Chinese content on the website. No English content.
The registration forms needs to be designed and include in the final deliverable.

```html
<!DOCTYPE html>
<html lang="en">
<head>
<meta charset="utf-8">
<title>TIKLOOMTOT</title>
<link href="https://fonts.googleapis.com/css2?family=Roboto:wght@400;500;700&family=Alfa+Slab+One&display=swap" rel="stylesheet">
<style>
:root{
  --pink:#e0245e;
  --red:#d8262b;
  --blue:#0592cd;
  --blue-dark:#0355a3;
  --blue-mid:#3277b5;
  --blue-light:#cee9f5;
  --sky:#85cae6;
  --cream:#f4ecd9;
  --lilac:#dcdbe9;
  --ink:#333;
  --grey:#777;
  --footer:#2a2a2a;
  --white:#fff;
}
*{box-sizing:border-box;margin:0;padding:0}
html,body{width:724px;height:1200px;overflow:hidden;background:var(--white)}
body{font-family:'Roboto',Arial,sans-serif;color:var(--ink);position:relative}
section,header,footer{position:absolute;left:0;width:724px}

.site-nav{top:0;height:43px;background:var(--white);box-shadow:0 1px 3px rgba(0,0,0,.12);z-index:2}
.brand-mark{position:absolute;left:22px;top:4px;width:36px;height:36px;border-radius:50%;background:var(--pink)}
.brand-tab{position:absolute;left:70px;top:0;width:140px;height:43px;background:var(--pink);color:var(--white);font-weight:700;font-size:12px;line-height:43px;text-align:center}
.menu{position:absolute;left:240px;top:0;display:flex;gap:20px;height:43px;align-items:center;font-size:10px;font-weight:500;color:var(--grey)}
.chat-btn{position:absolute;right:26px;top:9px;width:66px;height:25px;background:#444;color:var(--white);font-size:9px;font-weight:700;line-height:25px;text-align:center}

.hero{top:43px;height:362px;background:linear-gradient(180deg,#f6fbfe 0%,#dcedf8 100%);overflow:hidden}
.hero-title{position:absolute;left:150px;top:100px;font-family:'Alfa Slab One',Georgia,serif;font-size:24px;font-weight:400;color:var(--red);letter-spacing:.5px}
.hero-text{position:absolute;left:150px;top:136px;width:250px;font-size:12px;font-weight:700;line-height:16px;color:#444}
.read-more{position:absolute;left:150px;top:200px;width:86px;height:22px;background:var(--blue-dark);color:var(--white);font-size:9px;font-weight:700;line-height:22px;padding-left:12px}
.product-bear{position:absolute;left:434px;top:6px;width:206px;height:338px;border-radius:60px 60px 24px 24px;background:linear-gradient(180deg,#cfe3f5 0%,#a9cbeb 55%,#c4dcf1 100%)}
.product-bag{position:absolute;left:290px;top:186px;width:140px;height:156px;border-radius:4px;background:linear-gradient(160deg,#4fa3dc,#e7b43c 55%,#e05a7c);z-index:1}
.arrow{position:absolute;top:190px}

.about{top:405px;height:148px;text-align:center}
.section-title{font-family:'Roboto',Arial,sans-serif;font-weight:700;font-size:22px;color:var(--red);letter-spacing:1px}
.about .section-title{margin-top:22px}
.rule{width:60px;height:2px;background:var(--red);margin:8px auto 14px}
.about p{width:560px;margin:0 auto;font-size:8.5px;line-height:13px;color:#555}

.experts{top:553px;height:200px;background:var(--cream)}
.expert{position:absolute;top:24px;width:150px;text-align:center;margin-left:-75px}
.expert .portrait{width:98px;height:98px;border-radius:50%;margin:0 auto;border:4px solid var(--white);box-shadow:0 0 0 1px #d8cfb8;background:linear-gradient(180deg,#c9b8a3,#8a7766)}
.expert h3{margin-top:12px;font-size:10px;font-weight:700;color:var(--pink)}
.expert p{margin-top:5px;font-size:8px;line-height:11px;color:#555}

.showcase{top:753px;height:245px;background:var(--lilac)}
.item{position:absolute;top:28px;width:168px}
.item .photo{height:124px;border:4px solid var(--white);background:linear-gradient(160deg,#e9c6d4,#c9d9e8)}
.item h4{margin-top:10px;font-size:9px;font-weight:700;color:var(--pink)}
.item p{margin-top:4px;font-size:7.5px;line-height:10px;color:#555}
.order-form{position:absolute;left:482px;top:22px;width:182px;height:212px;background:var(--white);box-shadow:0 1px 4px rgba(0,0,0,.15)}
.order-form .form-head{height:26px;background:var(--red);color:var(--white);font-size:10px;font-weight:700;line-height:26px;text-align:center}
.field{margin:8px 12px 0;height:15px;border:1px solid #ccc;font-size:7px;color:#999;line-height:13px;padding-left:5px}
.field.tall{height:30px}
.order-btn{margin:10px auto 0;width:70px;height:18px;background:var(--red);color:var(--white);font-size:8px;font-weight:700;line-height:18px;text-align:center}

.site-footer{top:998px;height:137px;background:linear-gradient(180deg,var(--blue-mid),var(--blue));color:var(--white)}
.col{position:absolute;top:20px;width:160px}
.col h5{font-size:13px;font-weight:500;letter-spacing:.5px;margin-bottom:10px}
.col p{font-size:7.5px;line-height:11px;opacity:.9}
.col .date{font-size:7px;opacity:.75;margin-top:6px}
.signup{display:flex;margin-top:10px}
.signup span{width:120px;height:16px;background:var(--white);color:#999;font-size:7px;line-height:16px;padding-left:5px}
.signup b{width:34px;height:16px;background:var(--blue-dark);font-size:7px;line-height:16px;text-align:center}

.base-bar{top:1135px;height:65px;background:var(--footer);color:#ccc}
.base-links{position:absolute;left:108px;top:16px;font-size:8px;font-weight:500;color:var(--white);word-spacing:4px}
.base-copy{position:absolute;left:108px;top:32px;font-size:7px;color:#999}
.social-label{position:absolute;left:420px;top:26px;font-size:8px;font-weight:500;color:var(--white)}
.social{position:absolute;left:500px;top:17px;display:flex;gap:6px}
.social i{width:24px;height:24px;border-radius:50%;background:var(--white);display:block}
</style>
</head>
<body>

<header class="site-nav">
  <div class="brand-mark"></div>
  <div class="brand-tab">TIKLOOMTOT</div>
  <nav class="menu"><span>ORDER NOW</span><span>ABOUT US</span><span>OUR EXPERTS</span><span>FAQ</span><span>SHARE</span></nav>
  <div class="chat-btn">TALKBOX</div>
</header>

<section class="hero">
  <svg class="arrow" style="left:66px" width="16" height="26" viewBox="0 0 16 26"><path d="M13 2 L3 13 L13 24" stroke="#333" stroke-width="3" fill="none"/></svg>
  <h1 class="hero-title">TIKLOOMTOT</h1>
  <p class="hero-text">Lorem Ipsum is simply dummy text of the printing and typesetting industry</p>
  <div class="read-more">READ MORE ▸</div>
  <div class="product-bear" role="img" aria-label="Soft blue teddy bear toy"></div>
  <div class="product-bag" role="img" aria-label="Colourful gift bag filled with children's books"></div>
  <svg class="arrow" style="left:648px" width="16" height="26" viewBox="0 0 16 26"><path d="M3 2 L13 13 L3 24" stroke="#333" stroke-width="3" fill="none"/></svg>
</section>

<section class="about">
  <h2 class="section-title">ABOUT US</h2>
  <div class="rule"></div>
  <p>Cradleleaf Book Club - let the children stay at home and enjoy the best the world of reading has to offer. Each month families receive a box of books, toys and crafts chosen for their child's age and interests. Subscribe now to our monthly boxes and open a new world of stories, play and learning for your little one, with notes from our experts in every box delivered right to your door.</p>
</section>

<section class="experts">
  <div class="expert" style="left:180px">
    <div class="portrait" role="img" aria-label="Portrait photo of expert"></div>
    <h3>LIN MEIQI, MD</h3>
    <p>Northbrook Children's Hospital<br>pediatrician and physician</p>
  </div>
  <div class="expert" style="left:335px">
    <div class="portrait" role="img" aria-label="Portrait photo of expert"></div>
    <h3>DR. OWEN R. TALBOT</h3>
    <p>Northbrook Children's Hospital<br>pediatrician and physician</p>
  </div>
  <div class="expert" style="left:490px">
    <div class="portrait" role="img" aria-label="Portrait photo of expert"></div>
    <h3>HAZEL PREWITT</h3>
    <p>Northbrook Children's Hospital<br>pediatrician and physician</p>
  </div>
  <div class="expert" style="left:645px">
    <div class="portrait" role="img" aria-label="Portrait photo of expert"></div>
    <h3>IVO BRANDEL</h3>
    <p>Northbrook Children's Hospital<br>pediatrician and physician</p>
  </div>
</section>

<section class="showcase">
  <div class="item" style="left:108px">
    <div class="photo" role="img" aria-label="Pink teddy bear with a gift box"></div>
    <h4>IPSUM IS SIMPLY DUMMY TEXT</h4>
    <p>Lorem ipsum has been the industry's standard dummy text ever since the 1500s, when an unknown printer took a galley of type and scrambled it to make a specimen book.</p>
  </div>
  <div class="item" style="left:290px">
    <div class="photo" role="img" aria-label="Open box of children's books and toys"></div>
    <h4>IPSUM IS SIMPLY DUMMY TEXT</h4>
    <p>Lorem ipsum has been the industry's standard dummy text ever since the 1500s, when an unknown printer took a galley of type and scrambled it to make a specimen book.</p>
  </div>
  <form class="order-form">
    <div class="form-head">ORDER NOW</div>
    <div class="field">Name</div>
    <div class="field">Email</div>
    <div class="field">Phone</div>
    <div class="field">Child's age</div>
    <div class="field">Gender</div>
    <div class="field tall">Interests</div>
    <div class="order-btn">ORDER NOW</div>
  </form>
</section>

<footer class="site-footer">
  <div class="col" style="left:108px">
    <h5>LATEST NEWS</h5>
    <p>New spring box ships soon with picture books and craft kits.</p>
    <p class="date">03 MARCH 2014</p>
    <p>Meet our experts at the family reading day this weekend.</p>
    <p class="date">21 FEBRUARY 2014</p>
  </div>
  <div class="col" style="left:290px">
    <h5>GET IN TOUCH</h5>
    <p>18 Willow Lane, Harbor Park</p>
    <p>Phone: 000-555-0142</p>
    <p>Email: hello@tikloomtot.com</p>
  </div>
  <div class="col" style="left:458px">
    <h5>NEWSLETTER</h5>
    <p>Join our mailing list to stay up to date and get our news and special offers.</p>
    <div class="signup"><span>email address</span><b>JOIN</b></div>
  </div>
</footer>

<footer class="base-bar">
  <div class="base-links">HOME | ABOUT | PRODUCTS | BLOG | CONTACTS</div>
  <div class="base-copy">© 2014 Privacy Policy</div>
  <div class="social-label">SOCIAL NETWORKS</div>
  <div class="social"><i></i><i></i><i></i><i></i></div>
</footer>

</body>
</html>
```